Vitalune - Label design for a supplement with probiotic and prebiotic

Hello, we are a supplement company and we need a label design for our first product. The product's name is Vitalune and the company's name is Koravex Nutrition (Logo attached, It is allowed to change the color) and we are located in Orlando, if we like the label, in the future we can make other products too.
Our product is a supplement that contains probiotics, prebiotics and other vitamins, it will be packaged in a 300g plastic jar (Img attached), we like simple but premium-looking packaging.
Below are some links to brands and products we like:
https://www.shopvarelt.example/stores/page/7D1188AA-5521-4E9B-B302-B1A447FE22CC?ingress=2&visitId=91b2ccd4-774e-408a-bb21-c4e8f1aa2093&ref_=bl_dp_s_web_58213044022
https://www.shopvarelt.example/stores/page/61AB4E3D-92C1-4A77-9D20-7EE350173B81?ingress=2&visitId=8812fa0e-311c-4d2a-a7f4-1b9c30e44f12&ref_=bl_dp_s_web_24417720933
https://www.shopvarelt.example/stores/Teluvo+Nutrition/page/C2288340-5E61-4B19-93A4-12307C88D29E?store_ref=SLP_FW_450D77AB-C12E-4A98-A31F-2207E5C9A611
https://www.shopvarelt.example/stores/page/AA2C46DE-71F9-4B22-C390-5EEDC81B309F?ingress=2&visitId=15e93b27-6a0c-4f3e-9bd1-a7c2301ee9b4&ref_=bl_dp_s_web_4182930055
https://www.shopvarelt.example/stores/node/39527164022?_encoding=UTF8&field-lbr_brands_browse-bin=QUILMAXNUTRITION&ref_=bl_dp_s_web_39527164022
https://www.shopvarelt.example/stores/page/2B3E8804-6611-4C2A-9F17-E8A913B02C57?ingress=6&visitId=4461d09c-b12a-4d7e-8fa1-09c5d3e6bb21&store_ref=storeRecs_Instant_27316488033
Updates
Hi, This product will be packaged in a 300g bottle, it is allowed to insert images and it is very important to inform "100 Billion live bacteria", 5 grams of probiotic, 5 grams of prebiotic and orange flavor.
The bottle is rounded, the size of the art must be 2.87 in and 10.74 in, I will need barcode space, supplement facts, directions and warning. This information I can put later.
Target Market(s)
Our target is people who wish to have a healthier recovery after undergoing cancer treatments, helping to maintain health, improving quality of life and reducing the harm that these treatments cause.
Requirements
Must have
- It is very important that the product contains the following information:
- 100 Billion live bacteria
- 5 grams of probiotic and 5 grams of prebiotic
- No artificial flavours
- Space for barcode
Amount per container: 10.6 oz (300 g)
Serving size: 1 scoop (10 grams)
Servings per container: 30
Amount per serving
Calories 15 Calories from fat 0
Total Fat 0
Total Carbohydrate 5g
Dietary fiber 4g
Sugars 1g
Protein 0g
Proprietary Probiotic blend: 5 billons
Lactobacillus acidophilus
Bifidobacterium animalis subsp. lactis.
Other ingredients: Organic inulin fiber, stevia, natural orange flavor, citric acid, riboflavin Not a significant source of cholesterol, fat and protein
Nice to have
- We like simple design
Should not have
- Images from brolen photos.

```html
<!DOCTYPE html>
<html lang="en">
<head>
<meta charset="utf-8">
<title>Vitalune – Probiotics plus Prebiotics Label</title>
<link rel="stylesheet" href="https://fonts.googleapis.com/css2?family=Lexend:wght@400;500;700;800&display=swap">
<style>
  :root {
    --backdrop: #eaedf2;
    --label-blue: #63b4d4;
    --label-blue-light: #7cc6e0;
    --label-blue-deep: #3fa3cc;
    --accent-green: #b8d840;
    --band-green: #a9cf48;
    --badge-fill: #c8e27a;
    --badge-ink: #3aa6cf;
    --tag-red: #d85a6a;
    --ink-white: #ffffff;
    --brand-blue: #2aa9d8;
  }
  * { margin: 0; padding: 0; box-sizing: border-box; }
  html, body {
    width: 1200px; height: 1200px; overflow: hidden;
    background: var(--backdrop);
    font-family: "Lexend", "Helvetica Neue", Arial, sans-serif;
  }
  .canvas {
    position: relative; width: 1200px; height: 1200px;
    display: flex; align-items: center; justify-content: center;
  }
  .label {
    position: relative; width: 1080px; height: 640px;
    background: linear-gradient(160deg, var(--label-blue-light) 0%, var(--label-blue) 55%, var(--label-blue-deep) 100%);
    border-radius: 6px; overflow: hidden;
  }
  .brand-line {
    position: absolute; left: 80px; top: 60px;
    color: var(--ink-white); font-weight: 700; font-size: 24px;
    letter-spacing: 0.08em; text-transform: uppercase;
  }
  .pattern-area {
    position: absolute; right: 0; top: 0; width: 420px; height: 500px;
    background: radial-gradient(circle at 60% 45%, rgba(200,226,122,0.28) 0%, rgba(200,226,122,0) 70%);
  }
  .flavour {
    position: absolute; left: 80px; top: 170px;
    color: var(--ink-white); font-weight: 400; font-size: 26px; letter-spacing: 0.02em;
  }
  .product-name {
    position: absolute; left: 76px; top: 205px;
    color: var(--accent-green); font-weight: 800; font-size: 112px; letter-spacing: 0.01em; line-height: 1;
  }
  .product-type {
    position: absolute; left: 80px; top: 330px;
    color: var(--ink-white); font-weight: 700; font-size: 44px; letter-spacing: 0.01em;
  }
  .strain-tag {
    position: absolute; left: 110px; top: 400px;
    background: var(--tag-red); color: var(--ink-white);
    font-weight: 400; font-size: 30px; padding: 6px 22px;
  }
  .badge {
    position: absolute; right: 90px; top: 70px; width: 320px; height: 320px;
  }
  .info-band {
    position: absolute; left: 0; bottom: 0; width: 100%; height: 140px;
    background: var(--band-green);
    display: flex; align-items: center; justify-content: space-between;
    padding: 0 80px;
  }
  .dose {
    color: var(--ink-white); font-weight: 400; font-size: 30px; opacity: 0.9;
  }
  .net-weight {
    color: var(--ink-white); font-weight: 700; font-size: 40px;
  }
</style>
</head>
<body>
<main class="canvas">
  <section class="label">
    <div class="pattern-area" role="img" aria-label="Faint hexagon molecule pattern behind the badge"></div>
    <p class="brand-line">Koravex Nutrition</p>
    <p class="flavour">natural orange flavour</p>
    <h1 class="product-name">Vitalune</h1>
    <p class="product-type">probiotics plus prebiotics</p>
    <p class="strain-tag">100 billion probiotic strain</p>

    <svg class="badge" viewBox="0 0 320 320" aria-label="Supports digestive health, wellness, immunity">
      <defs>
        <path id="badge-ring" d="M160,160 m-118,0 a118,118 0 1,1 236,0 a118,118 0 1,1 -236,0"/>
      </defs>
      <circle cx="160" cy="160" r="150" fill="var(--badge-fill)" opacity="0.85"/>
      <text font-family="Lexend, sans-serif" font-size="25" fill="var(--badge-ink)" letter-spacing="1">
        <textPath href="#badge-ring" startOffset="0">supports digestive health • wellness • immunity •</textPath>
      </text>
      <circle cx="160" cy="160" r="80" fill="#d8ec9c" role="img" aria-label="Outline icon of a stomach"/>
    </svg>

    <footer class="info-band">
      <p class="dose">5 gr probiotic + 5 gr prebiotic</p>
      <p class="net-weight">10.6 oz (300 g)</p>
    </footer>
  </section>
</main>
</body>
</html>
```